Dentist Home Page Design

We need a home page design to be used as a responsive wordpress theme for our dentist website. Website overall look and feel should look professional, yet very friendly as going to dentist is not people's favorite thing to do, for most it might even be scary. We want our website to differentiate with its design from all other generic looking cookie cutter dentists and creates a branded feel.
you can use a generic image for the 680x300px banner on the home pageif you like in the meantime). Total width should not exceed 960 px
Please follow the layout on the wireframes, do not add or delete random elements.
Target Market(s)
mostly targets male/female between 30-45, families with kids as well.
Industry/Entity Type
It Professional
Colors
Designer to choose colors to be used in the design.
Look and feel
Each slider illustrates characteristics of the customer's brand and the style your logo design should communicate.

```html
<!DOCTYPE html>
<html lang="en">
<head>
<meta charset="utf-8">
<title>Brightway Dental – Home</title>
<link href="https://fonts.googleapis.com/css2?family=Source+Sans+3:wght@400;600;700&display=swap" rel="stylesheet">
<style>
:root{
  --blue:#1d4fa8;
  --blue-light:#2a63c4;
  --blue-dark:#17418f;
  --navy:#0a1630;
  --orange:#f07a1a;
  --orange-dark:#e0620f;
  --orange-text:#ee6c14;
  --grey:#d5d5d5;
  --white:#ffffff;
  --text-dark:#1f3f86;
}
*{margin:0;padding:0;box-sizing:border-box}
html,body{width:1200px;height:900px;overflow:hidden;background:var(--white);font-family:"Source Sans 3",sans-serif}
.page{position:relative;width:1200px;height:900px}

.brand{position:absolute;left:118px;top:18px;width:302px;height:158px}
.brand-name{position:absolute;left:14px;top:6px;font-size:30px;font-weight:700;color:var(--text-dark);line-height:1;width:160px}
.brand-dot{position:absolute;left:178px;top:10px;width:22px;height:22px;border-radius:50%;background:var(--orange)}
.brand-doctor{position:absolute;left:40px;top:72px;font-size:25px;font-weight:600;color:var(--text-dark);letter-spacing:.5px}
.brand-rule{position:absolute;left:0;top:108px;width:302px;height:1px;background:var(--orange)}
.brand-role{position:absolute;left:40px;top:114px;font-size:12px;color:var(--text-dark)}
.brand-ortho{position:absolute;left:200px;top:116px;font-size:12px;color:var(--text-dark);line-height:1.3;text-align:left}
.brand-ortho small{font-size:10.5px}

.share{position:absolute;top:18px;left:820px;display:flex;gap:8px}
.share-btn{display:flex;align-items:center;height:18px}
.share-label{border:1px solid #b9c4d8;background:#eef1f7;border-radius:3px;font-size:11px;font-weight:700;color:#3b5592;padding:0 5px;line-height:16px}
.share-count{border:1px solid #ccc;border-radius:2px;font-size:10px;color:#777;padding:0 4px;line-height:14px;margin-left:4px}
.social{position:absolute;top:46px;left:907px;display:flex;gap:8px}
.social span{width:28px;height:28px;border-radius:50%;background:var(--grey)}

.call{position:absolute;right:120px;top:94px;text-align:right;color:var(--orange-text)}
.call-line{display:flex;align-items:baseline;gap:12px;justify-content:flex-end}
.call-link{font-size:13px;text-decoration:underline}
.call-number{font-size:30px}
.call-request{font-size:13px;text-decoration:underline;display:block;margin-top:-2px}

.nav{position:absolute;left:119px;top:200px;width:960px;height:50px;display:flex;background:linear-gradient(var(--blue-light),var(--blue-dark))}
.nav a{color:var(--white);text-decoration:none;font-size:15px;display:flex;align-items:center;justify-content:center;border-right:1px solid rgba(255,255,255,.18);height:100%}
.nav a.active{background:linear-gradient(#f58a2c,var(--orange-dark))}

.banner{position:absolute;left:120px;top:270px;width:679px;height:300px;background:linear-gradient(110deg,#e8eef2 0%,#c9dbe6 40%,#e7c2b0 75%,#d9a894 100%)}

.consult{position:absolute;left:799px;top:270px;width:280px;height:300px;background:linear-gradient(var(--orange),var(--orange-dark));color:var(--white)}
.consult h2{font-size:18px;font-weight:400;padding:10px 19px;height:40px;border-bottom:1px solid rgba(255,255,255,.25);background:#f4872c}
.consult form{padding:9px 20px 0}
.consult label{display:block;font-size:11.5px;letter-spacing:.3px;margin-bottom:3px}
.consult .field{width:220px;height:28px;background:var(--white);margin-bottom:8px;border:0;display:block}
.consult .pair{display:flex;gap:4px}
.consult .pair span{width:108px;height:28px;background:var(--white);color:var(--orange-text);font-style:italic;font-size:12px;padding:7px 9px}
.consult .submit{margin:14px 0 0 111px;width:109px;height:28px;background:linear-gradient(#f99a45,var(--orange));color:var(--white);font-size:14px;display:flex;align-items:center;justify-content:center;border-radius:2px}

.intro-band{position:absolute;left:0;top:610px;width:1200px;height:290px;background:linear-gradient(var(--blue-dark),var(--blue))}
.intro{position:absolute;left:141px;top:18px;width:510px;color:var(--white)}
.intro h1{font-size:20px;font-weight:700;padding-bottom:8px;border-bottom:1px solid rgba(255,255,255,.2);margin-bottom:12px}
.intro p{font-size:13.5px;line-height:1.27;margin-bottom:16px}
.video{position:absolute;left:699px;top:0;width:380px;height:290px;background:var(--navy)}
.video svg{position:absolute;left:149px;top:104px}
</style>
</head>
<body>
<div class="page">
  <header>
    <div class="brand">
      <div class="brand-name">Brightway Dental</div>
      <span class="brand-dot"></span>
      <div class="brand-doctor">Dr. Paul Arden</div>
      <div class="brand-rule"></div>
      <div class="brand-role">General Dentist</div>
      <div class="brand-ortho">Orthodontics<br><small>for Adults &amp; Children</small></div>
    </div>

    <div class="share">
      <div class="share-btn"><span class="share-label">Share</span><span class="share-count">36</span></div>
      <div class="share-btn"><span class="share-label">Post</span><span class="share-count">39</span></div>
      <div class="share-btn"><span class="share-label" style="color:#d8452c">Plus</span></div>
    </div>
    <div class="social"><span></span><span></span><span></span><span></span><span></span></div>

    <div class="call">
      <div class="call-line"><span class="call-link">Click to call</span><span class="call-number">(555) 014-2288</span></div>
      <span class="call-request">Request a free consultation</span>
    </div>
  </header>

  <nav class="nav">
    <a class="active" style="width:104px">Home</a>
    <a style="width:105px">About us</a>
    <a style="width:122px">Our Services</a>
    <a style="width:143px">Our Technology</a>
    <a style="width:118px">Dental Care</a>
    <a style="width:124px">Case Studies</a>
    <a style="width:126px">New Patients</a>
    <a style="width:118px;border-right:0">Contact</a>
  </nav>

  <div class="banner" role="img" aria-label="Smiling patient during a dental check-up"></div>

  <aside class="consult">
    <h2>Request a Free Consultation</h2>
    <form>
      <label>Your Full Name</label><span class="field"></span>
      <label>Your Phone Number</label><span class="field"></span>
      <label>Your Best Email</label><span class="field"></span>
      <label>Preferred Date &amp; Time</label>
      <div class="pair"><span>Date</span><span>Time</span></div>
      <div class="submit">Submit</div>
    </form>
  </aside>

  <section class="intro-band">
    <div class="intro">
      <h1>Your Experience In Dentistry Begins Now!</h1>
      <p>Focusing entirely on your comfort and convenience, Dr. Paul Arden, General Dentist, and his staff have created a pleasant place where dentistry is matched with a cozy, “at home” atmosphere. It’s a place where you can watch TV wearing virtual reality glasses while we take care of your teeth.</p>
      <p>Relax by the fireplace and let your little ones play with the toys and video games in our reception area (the toys are for the big kids, too). Evening and Saturday appointments are also available, and there’s always ample free parking.</p>
      <p>This website is only an introduction. We encourage you to call or visit our office and talk to our staff and Dr. Paul today.</p>
    </div>
    <div class="video">
      <svg width="82" height="82" viewBox="0 0 82 82" aria-label="Play video">
        <circle cx="41" cy="41" r="38" fill="none" stroke="#fff" stroke-width="4"/>
        <path d="M34 25 L52 41 L34 57 Z" fill="#fff"/>
      </svg>
    </div>
  </section>
</div>
</body>
</html>
```